Proyecto Mandril
Stationary
Proyecto Mandril -
Creative Brief
Use specific fonts
Century Gothic
Professional
Ramón Ignacio Bertoldi
Urb. Miraflores Calle Los Pinos Casa 27C Panamá City Panamá
ramon@lacasadelpanvivo.com
We have created business cards in the past and we would like to keep some consistency. We are uploanding those for your reference (front and back of the card). However, we only have business cards, we don't have other stationary and we are looking for a complete set. Thanks for considering our project and we look foraward to receiving your drafts. Best, Talia & Nora
www.lacasadelpanvivo.com

```html
<!DOCTYPE html>
<html lang="es">
<head>
<meta charset="utf-8">
<title>Proyecto Mandril — Papelería</title>
<link href="https://fonts.googleapis.com/css2?family=Questrial&display=swap" rel="stylesheet">
<style>
  :root {
    --paper: #ffffff;
    --backdrop: #ffffff;
    --frame: #3d3d3d;
    --ink: #4a4a4a;
    --brand: #5a4632;
    --rule: #b49a7a;
    --shadow: rgba(0, 0, 0, 0.22);
  }
  * { margin: 0; padding: 0; box-sizing: border-box; }
  html, body {
    width: 1200px;
    height: 681px;
    overflow: hidden;
    background: var(--backdrop);
    font-family: "Questrial", "Century Gothic", sans-serif;
    color: var(--ink);
  }
  .stationery-set { position: relative; width: 1200px; height: 681px; }

  .sheet {
    position: absolute;
    background: var(--paper);
    box-shadow: 2px 3px 6px var(--shadow);
    overflow: hidden;
  }
  .sheet--framed { border: 4px solid var(--frame); }

  /* brand lockup */
  .brand {
    position: absolute;
    display: flex;
    align-items: center;
    gap: 5px;
    color: var(--brand);
    font-size: 11px;
    line-height: 1.05;
    letter-spacing: 0.02em;
  }
  .brand__mark {
    flex: none;
    width: 14px;
    height: 14px;
    background: var(--brand);
  }
  .brand--small { font-size: 8px; gap: 4px; }
  .brand--small .brand__mark { width: 10px; height: 10px; }

  .divider {
    position: absolute;
    width: 1px;
    background: var(--rule);
  }
  .details {
    position: absolute;
    font-size: 6.5px;
    line-height: 1.45;
    font-style: normal;
    color: var(--ink);
    white-space: nowrap;
  }

  /* envelope front */
  .envelope-front { left: 67px; top: 96px; width: 528px; height: 216px; }
  .envelope-front .brand { left: 12px; top: 22px; }
  .envelope-front .divider { left: 88px; top: 16px; height: 54px; }
  .envelope-front .details { left: 94px; top: 18px; }

  /* envelope back */
  .envelope-back { left: 67px; top: 348px; width: 528px; height: 228px; border: 1px solid #9a9a9a; }
  .envelope-back__flap { position: absolute; left: 0; top: 0; width: 100%; height: 60px; }
  .envelope-back .brand { left: 50%; top: 10px; transform: translateX(-50%); }

  /* letterhead */
  .letterhead { left: 619px; top: 48px; width: 324px; height: 576px; }
  .letterhead .brand { left: 14px; top: 36px; }
  .letterhead .divider { left: 98px; top: 26px; height: 66px; }
  .letterhead .details { left: 104px; top: 28px; }

  /* business card */
  .card-front { left: 967px; top: 168px; width: 156px; height: 125px; }
  .card-front .brand { left: 7px; top: 22px; font-size: 8px; gap: 4px; }
  .card-front .brand .brand__mark { width: 10px; height: 10px; }
  .card-front .divider { left: 58px; top: 14px; height: 92px; }
  .card-front .card-name { position: absolute; left: 63px; top: 22px; font-size: 5.5px; line-height: 1.3; color: var(--ink); white-space: nowrap; }
  .card-front .details { left: 63px; top: 74px; font-size: 5.2px; }

  .card-back { left: 967px; top: 307px; width: 156px; height: 120px; }
  .card-back__site {
    position: absolute; left: 0; right: 0; top: 50%;
    transform: translateY(-50%);
    text-align: center;
    font-size: 6px;
    color: var(--ink);
  }
</style>
</head>
<body>
<main class="stationery-set">

  <section class="sheet sheet--framed envelope-front" aria-label="Sobre, cara frontal">
    <div class="brand"><span class="brand__mark"></span><span>Proyecto<br>Mandril</span></div>
    <div class="divider"></div>
    <address class="details">
      Urb. Miraflores<br>Calle Los Pinos<br>Casa 27C<br>Panamá City
    </address>
  </section>

  <section class="sheet envelope-back" aria-label="Sobre, reverso">
    <svg class="envelope-back__flap" viewBox="0 0 528 60" preserveAspectRatio="none" aria-hidden="true">
      <polyline points="0,0 36,52 492,52 528,0" fill="none" stroke="#8a8a8a" stroke-width="1"/>
    </svg>
    <div class="brand brand--small"><span class="brand__mark"></span><span>Proyecto Mandril</span></div>
  </section>

  <section class="sheet sheet--framed letterhead" aria-label="Hoja membretada">
    <div class="brand"><span class="brand__mark"></span><span>Proyecto<br>Mandril</span></div>
    <div class="divider"></div>
    <address class="details">
      Urb. Miraflores<br>Calle Los Pinos<br>Casa 27C<br>Panamá City<br>
      Tel: +507 264 5512<br>Cel: +507 6612 4480<br>ramon@lacasadelpanvivo.com
    </address>
  </section>

  <section class="sheet sheet--framed card-front" aria-label="Tarjeta de presentación, frente">
    <div class="brand"><span class="brand__mark"></span><span>Proyecto<br>Mandril</span></div>
    <div class="divider"></div>
    <p class="card-name">Ramón Ignacio Bertoldi</p>
    <address class="details">
      Tel: +507 264 5512<br>Cel: +507 6612 4480<br>ramon@lacasadelpanvivo.com
    </address>
  </section>

  <section class="sheet sheet--framed card-back" aria-label="Tarjeta de presentación, reverso">
    <p class="card-back__site">www.lacasadelpanvivo.com</p>
  </section>

</main>
</body>
</html>
```